QLV Fashion Design Company Needs a New Web Design, Please Click Me

Designers:

PLEASE NOTE: we only need the web page design, not a fully coded website.

Our brand's name is The Bright Quarry, our signature is print. our style is edgy and chic.

The old website is too messy. here's the address:
www.qlvstudio.com.cn

The new website's purpose is to show our brand/design and most importantly, sell products, So it should be a combination of a designer official website and online shopping. I want the whole style to be clean, edgy and pioneer, easy to understand. we need a sophisticated online shopping website.

The reference websites are:
merolatest.co.uk
www.pd-kor.com
lucasvemm.com
orbaduvi.com
talumerosapkin.com

Please beat their designs :)

Check out our lasted fashion show to get to know us more.

https://www.vidplexa.com/watch?v=ZkamWtrBnoLe&spfreload=10

The attachments are our Logo and some 2015 Look Book.
(Please let us know if you want to play with our print in this particular web design, we can send the source file.)
Updates

Designers, we really like the design of ameliadrovenko.com(we have attached a picture of the website) , Can we get a homepage like that? so the designs you submit will be 3 pages. The first one should be a page that only has Shop/Look. then the shop page, it should be nothing but our product which we will list the categories ourself. And the look page should contain all the info. such as news, about us and designers etc. Thank you all for your hard work, we really enjoyed the designs. Added Monday, November 03, 2014

Target Market(s)

Our target audiences are woman aged from 16-40 who like online shopping

Industry/Entity Type

Online Shopping

Number of Pages Required

3 page

Font styles to use
Serif
Sans Serif
Script

Requirements
Must have
• Designers,
• we really like the design of ameliadrovenko.com(we have attached a picture of the website) , Can we get a homepage like that? so the designs you submit will be 3 pages. The first one should be a page that only has Shop/Look. then the shop page, it should be nothing but our product which we will list the categories ourself. And the look page should contain all the info. such as news, about us and designers etc. Thank you all for your hard work, we really enjoyed the designs.

```html
<!DOCTYPE html>
<html lang="en">
<head>
<meta charset="utf-8">
<title>QLV Group — The Bright Quarry</title>
<link href="https://fonts.googleapis.com/css2?family=Cinzel:wght@400&family=Dosis:wght@300;400;500;600&display=swap" rel="stylesheet">
<style>
  :root{
    --ink:#1d1d1d;
    --white:#ffffff;
    --accent:#b30d0d;
    --rule:#e6e6e6;
    --tab-text:#8a8a8a;
    --hero-dark:#0c0c0c;
    --footer-dark:#1a1816;
    --footer-rule:#4a4744;
    --field:#8e8c8a;
  }
  *{margin:0;padding:0;box-sizing:border-box}
  html,body{width:840px;height:1200px;overflow:hidden;background:var(--white)}
  body{position:relative;font-family:"Dosis",sans-serif;color:var(--ink)}
  .abs{position:absolute}

  /* hero */
  .hero{left:0;top:0;width:840px;height:234px;
    background:radial-gradient(ellipse at 45% 40%,#3a3836 0%,#1c1b1a 45%,var(--hero-dark) 100%)}
  .brand-mark{left:380px;top:30px;width:80px;height:80px;border-radius:50%;background:var(--white)}
  .brand-name{left:0;width:840px;text-align:center;font-family:"Cinzel",serif;color:var(--white);
    letter-spacing:1.5px;line-height:1}
  .brand-group{top:121px;font-size:18px}
  .brand-tag{top:140px;font-size:18px}
  .hero-btn{top:176px;width:74px;height:26px;border:1px solid var(--white);color:var(--white);
    font-size:13px;font-weight:500;text-align:center;line-height:24px;letter-spacing:.5px}
  .hero-btn.shop{left:326px}
  .hero-btn.menu{left:439px}
  .hero-slash{left:414px;top:181px;color:var(--white);font-size:13px}

  /* section heading */
  .rule{height:2px;background:var(--rule)}
  .section-title{left:0;width:840px;text-align:center;font-size:35px;font-weight:300;letter-spacing:.5px;line-height:1}
  .tab{width:89px;height:23px;border:1px solid var(--rule);font-size:7.5px;font-weight:500;
    text-align:center;line-height:21px;color:var(--tab-text);letter-spacing:.3px}
  .tab.active{background:var(--accent);border-color:var(--accent);color:var(--white)}

  /* product tiles */
  .tile{width:196px;height:235px}
  .price{left:44px;top:124px;width:107px;height:46px;border:1px solid var(--white);color:var(--white);
    font-size:20px;font-weight:500;text-align:center;line-height:44px}
  .zoom{left:77px;top:64px}
  .look-dark{background:linear-gradient(160deg,#1f2a3a,#0a0d14 70%)}
  .look-print{background:linear-gradient(170deg,#1d3a66,#b8a9a6 45%,#6d88b5 80%,#1c2f55)}
  .look-blue{background:linear-gradient(170deg,#142a52,#3f6fb8 50%,#243f78)}
  .print-dark{background:radial-gradient(circle at 50% 50%,#252a30,#0b0d10 80%)}
  .print-burst{background:radial-gradient(circle at 50% 50%,#ffffff 0%,#d9c7b0 35%,#a7825b 70%,#e6d2bd 100%)}
  .print-rays{background:radial-gradient(circle at 50% 45%,#cfe0f5 0%,#5b8fd3 35%,#204f99 75%,#16315f 100%)}

  /* footer */
  .footer{left:0;top:1024px;width:840px;height:176px;
    background:linear-gradient(90deg,#2b2622 0%,var(--footer-dark) 40%,#141312 70%,#2a2520 100%)}
  .foot-rule{height:1px;background:var(--footer-rule)}
  .foot-title{top:1061px;font-size:22px;font-weight:300;color:var(--white);letter-spacing:.3px;line-height:1}
  .social{left:122px;top:1114px;display:flex;gap:7px}
  .social-item{display:flex;align-items:center;gap:3px;color:#cfcfcf;font-size:10px;font-weight:500}
  .social-item i{width:12px;height:12px;border-radius:50%;background:#cfcfcf;display:block}
  .email-field{left:425px;top:1110px;width:218px;height:27px;background:var(--field);color:var(--white);
    font-size:8px;line-height:27px;padding-left:10px;letter-spacing:.3px}
  .email-icon{left:618px;top:1117px}
  .send-btn{left:647px;top:1110px;width:74px;height:27px;background:var(--accent);color:var(--white);
    font-size:9px;font-weight:600;text-align:center;line-height:27px;letter-spacing:.5px}
  .copyright{left:0;top:1175px;width:840px;text-align:center;font-size:8.5px;color:var(--white)}
</style>
</head>
<body>

<header class="abs hero" role="img" aria-label="Dark fashion photograph of models in coats as hero backdrop"></header>
<div class="abs brand-mark" aria-hidden="true"></div>
<div class="abs brand-name brand-group">QLV GROUP</div>
<div class="abs brand-name brand-tag">THE BRIGHT QUARRY</div>
<div class="abs hero-btn shop">SHOP</div>
<div class="abs hero-slash">/</div>
<div class="abs hero-btn menu">MENU</div>

<!-- categories -->
<div class="abs rule" style="left:231px;top:259px;width:378px"></div>
<h2 class="abs section-title" style="top:272px">CATEGORIES</h2>
<div class="abs rule" style="left:231px;top:315px;width:378px"></div>
<div class="abs tab active" style="left:231px;top:328px">READY TO WEAR</div>
<div class="abs tab" style="left:328px;top:328px">ACCESSORIES</div>
<div class="abs tab" style="left:424px;top:328px">EYEWEAR</div>
<div class="abs tab" style="left:520px;top:328px">DENIM</div>

<div class="abs tile look-dark" style="left:121px;top:377px" role="img" aria-label="Model in blue printed dress, dimmed on hover">
  <svg class="abs zoom" width="42" height="42" viewBox="0 0 42 42" aria-hidden="true">
    <circle cx="17" cy="17" r="13" fill="none" stroke="#fff" stroke-width="4"/>
    <line x1="26.5" y1="26.5" x2="38" y2="38" stroke="#fff" stroke-width="5" stroke-linecap="round"/>
  </svg>
  <div class="abs price">$ 123.45</div>
</div>
<div class="abs tile look-print" style="left:323px;top:377px" role="img" aria-label="Model in multicolour printed dress against blue foil"></div>
<div class="abs tile look-blue" style="left:524px;top:377px" role="img" aria-label="Model in blue streaked print dress against blue foil"></div>

<!-- new prints -->
<div class="abs rule" style="left:231px;top:643px;width:378px"></div>
<h2 class="abs section-title" style="top:656px">NEW PRINTS</h2>
<div class="abs rule" style="left:231px;top:699px;width:378px"></div>
<div class="abs tab active" style="left:231px;top:712px">READY TO WEAR</div>
<div class="abs tab" style="left:328px;top:712px">ACCESSORIES</div>
<div class="abs tab" style="left:424px;top:712px">EYEWEAR</div>
<div class="abs tab" style="left:520px;top:712px">DENIM</div>

<div class="abs tile print-dark" style="left:121px;top:760px" role="img" aria-label="Dark abstract print, dimmed on hover">
  <svg class="abs zoom" width="42" height="42" viewBox="0 0 42 42" aria-hidden="true">
    <circle cx="17" cy="17" r="13" fill="none" stroke="#fff" stroke-width="4"/>
    <line x1="26.5" y1="26.5" x2="38" y2="38" stroke="#fff" stroke-width="5" stroke-linecap="round"/>
  </svg>
  <div class="abs price">$ 123.45</div>
</div>
<div class="abs tile print-burst" style="left:323px;top:760px" role="img" aria-label="Symmetric multicolour burst print"></div>
<div class="abs tile print-rays" style="left:524px;top:760px" role="img" aria-label="Blue radiating streak print"></div>

<!-- footer -->
<footer class="abs footer" role="img" aria-label="Dimmed photograph of a model lounging on a tufted sofa"></footer>
<div class="abs foot-rule" style="left:121px;top:1052px;width:295px"></div>
<div class="abs foot-rule" style="left:425px;top:1052px;width:296px"></div>
<h3 class="abs foot-title" style="left:121px">KEEP IN TOUCH</h3>
<h3 class="abs foot-title" style="left:425px">SIGNUP OUR NEWSLETTER</h3>
<div class="abs foot-rule" style="left:121px;top:1092px;width:295px"></div>
<div class="abs foot-rule" style="left:425px;top:1092px;width:296px"></div>

<div class="abs social">
  <span class="social-item"><i></i>Circlo</span>
  <span class="social-item"><i></i>Chirpa</span>
  <span class="social-item"><i></i>Plusly</span>
  <span class="social-item"><i></i>Pinora</span>
  <span class="social-item"><i></i>Vidplexa</span>
</div>

<div class="abs email-field">ENTER YOUR EMAIL HERE</div>
<svg class="abs email-icon" width="16" height="13" viewBox="0 0 16 13" aria-hidden="true">
  <path d="M1 6 L15 1 L11 12 L8 8 Z M8 8 L15 1" fill="none" stroke="#fff" stroke-width="1.2" stroke-linejoin="round"/>
</svg>
<div class="abs send-btn">SEND</div>

<div class="abs foot-rule" style="left:121px;top:1163px;width:600px"></div>
<p class="abs copyright">Copyright @ 2014 The Bright Quarry All</p>

</body>
</html>
```